Ferncrest Dental, LLC business card project

Business card to be designed with current logo.
Dental office- please keep design of card that looks clean and professional.
Please include the following info:
Ferncrest Dental, LLC
Dr. Lorna Pettigrew
2871 Marlowe Street
Bethlehem, PA 18093
610-555-0193
ferncrestdental.office@examplemail.test
Hello everyone-
Reason: Just got back from overseas- will look at all designs and provide feedback. Thank you!
Reason: Polling my friends for the final selection-
thank you to all those that participated- so many talented designers!

```html
<!DOCTYPE html>
<html lang="en">
<head>
<meta charset="utf-8">
<title>Ferncrest Dental, LLC – Business Card</title>
<link rel="stylesheet" href="https://fonts.googleapis.com/css2?family=Questrial&family=PT+Sans:wght@700&display=swap">
<style>
  :root {
    --page-bg: #2e2e2e;
    --card-bg: #ffffff;
    --leaf-green: #6b9a2e;
    --lime: #bfcf00;
    --ink-grey: #555555;
    --white: #ffffff;
  }
  html, body {
    margin: 0;
    padding: 0;
    width: 1200px;
    height: 900px;
    overflow: hidden;
    background: var(--page-bg);
  }
  .canvas {
    width: 1200px;
    height: 900px;
    display: flex;
    align-items: center;
    justify-content: center;
  }
  .business-card {
    position: relative;
    width: 1080px;
    height: 599px;
    background: var(--card-bg);
    overflow: hidden;
  }
  .doctor-name {
    position: absolute;
    top: 52px;
    left: 0;
    right: 0;
    margin: 0;
    text-align: center;
    font-family: "PT Sans", Tahoma, sans-serif;
    font-weight: 700;
    font-size: 38px;
    color: var(--leaf-green);
  }
  .practice-name {
    position: absolute;
    top: 196px;
    left: 0;
    right: 0;
    display: flex;
    align-items: center;
    justify-content: center;
    gap: 22px;
    font-family: "Questrial", "Century Gothic", sans-serif;
    font-size: 74px;
    color: var(--leaf-green);
    letter-spacing: -1px;
  }
  .practice-mark {
    width: 40px;
    height: 40px;
    border-radius: 50%;
    background: var(--lime);
    flex: none;
  }
  .phone {
    position: absolute;
    top: 390px;
    left: 0;
    right: 0;
    display: flex;
    align-items: center;
    justify-content: center;
    gap: 10px;
    font-family: "Questrial", "Century Gothic", sans-serif;
    font-size: 34px;
    color: var(--ink-grey);
  }
  .contact-band {
    position: absolute;
    left: 0;
    right: 0;
    height: 68px;
    display: flex;
    align-items: center;
    justify-content: center;
    gap: 10px;
    font-family: "PT Sans", Tahoma, sans-serif;
    font-weight: 700;
    font-size: 29px;
    color: var(--white);
  }
  .contact-band--email { top: 455px; background: var(--lime); }
  .contact-band--address { top: 531px; background: var(--leaf-green); }
  .icon { flex: none; }
</style>
</head>
<body>
<main class="canvas">
  <article class="business-card">
    <h1 class="doctor-name">Dr. Lorna Pettigrew</h1>

    <div class="practice-name">
      <span class="practice-mark" aria-hidden="true"></span>
      <span>Ferncrest Dental, LLC</span>
    </div>

    <p class="phone">
      <svg class="icon" width="26" height="26" viewBox="0 0 26 26" aria-hidden="true">
        <circle cx="13" cy="13" r="13" fill="var(--leaf-green)"/>
        <path d="M9 7c1 0 2 2.5 2 3s-1.2 1-1 1.6c.6 1.6 1.8 2.8 3.4 3.4.6.2 1.1-1 1.6-1s3 1 3 2-1.5 2.5-2.6 2.3C11 17.5 8.5 15 7.7 10.6 7.5 9.5 8 7 9 7z" fill="#fff"/>
      </svg>
      610-555-0193
    </p>

    <div class="contact-band contact-band--email">
      <svg class="icon" width="24" height="16" viewBox="0 0 24 16" aria-hidden="true">
        <rect x="0" y="0" width="24" height="16" rx="2" fill="#fff"/>
        <path d="M1 1l11 8 11-8" fill="none" stroke="var(--lime)" stroke-width="2"/>
      </svg>
      ferncrestdental.office@examplemail.test
    </div>

    <div class="contact-band contact-band--address">
      <svg class="icon" width="20" height="28" viewBox="0 0 20 28" aria-hidden="true">
        <path d="M10 0C4.5 0 0 4.4 0 9.8 0 17 10 28 10 28s10-11 10-18.2C20 4.4 15.5 0 10 0z" fill="#fff"/>
        <circle cx="10" cy="9.8" r="4" fill="var(--leaf-green)"/>
      </svg>
      2871 Marlowe Street Bethlehem, PA 18093
    </div>
  </article>
</main>
</body>
</html>
```